Zielgruppe
Unsere Vorstellung währe eine Flyer Falzflyer DIN lang 6-seitig oder 4-seitig,
wir sind für alle Vorschläge offen.
Wir sind eine Umzugsfirma für Privatumzüge, Firmenumzüge und Personaldienstleistung und kümmern uns um alles was in einem Umzug anfällt bzw. verpacken der Möbel Auf und Abbau der Möbel, Einpackservice aller Haushaltsgegenstände, darüber hinaus stellen wir auch nur Umzugshelfer.
Montage von Neumöbel wie Wandbrook durch geschultes Personal.
Die Infos wie z.B E-Mail, und Telefon sollten auch auf das Produkt.
E-Mail : info@pkv-transporte.example
Tel. 0049 152 38847261
Adresse: Lerchenfeldweg 27
71686 Remseck am Neckar
Der Tex sollte noch enthalten:
Über uns:
PKV Transporte ist ein erfahrenes und kompetentes Umzugsunternehmen aus Ludwigsburg.
Innerhalb der Umzugsbranche reduzieren wir uns nicht nur auf Privatumzüge, den unsere Palette reicht vom Firmenumzug, Entrümpelung und Ankauf von gebrauchte Büromöbeln so wie Personaldienstleistung in der Möbelbrache.
Wir bieten Ihnen:
-TOP Qualität zu fairen Preisen
-Wissen aus jahrelanger Erfahrung
-persönliche Beratung von der Idee bis zum Umzug
-ausgebildete Fachkräfte für Montagearbeiten, Entrümpelung, Ein- und Auspackservice das alles mit den Modernsten und besten Werkzeugen.
-Terminsicherheit auch bei kurzfristigem Umzugswunsch
-Einen verlässlichen Umzugspartner
Privatumzüge:
Sie freuen sich auf Ihre neuen vier Wände.
Vorher steht eine Menge Arbeit ins Haus: Ihr Umzug.
Kein Problem, wir packen das für Sie an.
PKV Transporte macht Ihren Möbeln Beine !
Unser Leistungsspektrum umfasst alle Dienstleistungen rund um Ihren Umzug aus einer Hand:
Wir packen ein und aus, demontieren und montieren sämtliche Möbel,
leisten fachgerechte Schreiner-, Elektro- und Installationsarbeiten.
Bei uns sind Sie auf der sicheren Seite !
Es wird alles zu einem Festpreis..
Aufgabenstellung
Wir möchten das der Text Modern, kurz und knackig ist , darf auch etwas aus der reihe tanzen

```html
<!DOCTYPE html>
<html lang="de">
<head>
<meta charset="utf-8">
<title>PKV Transporte – Flyer</title>
<link href="https://fonts.googleapis.com/css2?family=Roboto:wght@400;700&family=Arimo:wght@400&display=swap" rel="stylesheet">
<style>
  :root {
    --slate: #56637f;
    --mover: #5f6f96;
    --orange: #ee7d1f;
    --white: #ffffff;
    --paper: #ffffff;
  }
  * { margin: 0; padding: 0; box-sizing: border-box; }
  html, body { width: 1200px; height: 1200px; overflow: hidden; background: var(--paper); }
  .flyer { position: relative; width: 1200px; height: 1200px; background: var(--paper); font-family: "Arimo", Arial, sans-serif; }

  .photo { position: absolute; }
  .photo-van { left: 79px; top: 110px; width: 257px; height: 171px; background: linear-gradient(135deg, #e9e4dc 0%, #c9a57a 55%, #3d4f8f 100%); }
  .photo-stairs { left: 349px; top: 110px; width: 171px; height: 171px; background: linear-gradient(160deg, #efefef 0%, #d8d8d8 50%, #34479a 100%); }

  .brand { position: absolute; left: 693px; top: 150px; width: 428px; height: 100px; display: flex; align-items: center; justify-content: center; gap: 14px; white-space: nowrap; }
  .brand-dot { flex: none; width: 20px; height: 20px; border-radius: 50%; background: var(--orange); }
  .brand-name { font-family: "Roboto", Arial, sans-serif; font-weight: 700; font-size: 42px; color: var(--slate); letter-spacing: 1px; text-transform: uppercase; }

  .slogan { position: absolute; left: 84px; top: 420px; font-family: "Roboto", Arial, sans-serif; font-weight: 700; font-size: 28px; line-height: 40px; color: var(--slate); text-transform: uppercase; }

  .about { position: absolute; left: 84px; top: 527px; width: 411px; font-size: 15px; line-height: 26px; color: var(--slate); }
  .about p + p { margin-top: 26px; }

  .contact-band { position: absolute; left: 0; top: 974px; width: 599px; height: 226px; background: var(--orange); }
  .contact { position: absolute; left: 144px; top: 1003px; font-size: 16px; line-height: 26px; color: var(--white); font-style: normal; }

  .mover-illustration { position: absolute; left: 402px; top: 903px; width: 116px; height: 262px; background: var(--mover); border-radius: 58px 58px 6px 6px; }

  .hero { position: absolute; left: 599px; top: 428px; width: 601px; height: 772px; background: linear-gradient(160deg, #ecebe8 0%, #e2d6c5 40%, #c9a57c 70%, #b7322f 100%); }
  .hero-quote { position: absolute; left: 617px; top: 474px; font-family: "Roboto", Arial, sans-serif; font-weight: 700; font-size: 28px; line-height: 40px; color: var(--white); text-transform: uppercase; text-shadow: 0 1px 3px rgba(0,0,0,0.35); }
</style>
</head>
<body>
<main class="flyer">
  <div class="photo photo-van" role="img" aria-label="Foto: zwei Umzugshelfer laden ein Regal aus einem Transporter, Umzugskartons daneben"></div>
  <div class="photo photo-stairs" role="img" aria-label="Foto: zwei Umzugshelfer tragen ein weißes Sofa ein Treppenhaus hinauf"></div>

  <div class="brand">
    <span class="brand-dot"></span>
    <span class="brand-name">PKV Transporte</span>
  </div>

  <h1 class="slogan">„Wir machen<br>Ihren Möbeln Beine“</h1>

  <section class="about">
    <p>PKV Transporte ist ein erfahrenes und kompetentes Umzugsunternehmen aus Ludwigsburg.</p>
    <p>Innerhalb der Umzugsbranche reduzieren wir uns nicht nur auf Privatumzüge, den unsere Palette reicht vom Firmenumzug, Entrümpelung und Ankauf von gebrauchte Büromöbeln so wie Personaldienstleistung in der Möbelbrache.</p>
  </section>

  <div class="contact-band"></div>
  <div class="mover-illustration" role="img" aria-label="Illustration: Umzugshelfer mit Mütze schiebt einen Plattformwagen"></div>
  <address class="contact">
    PKV Transporte<br>
    Lerchenfeldweg 27<br>
    71686 Remseck am Neckar<br>
    Tel. +49 152 38847261<br>
    info@pkv-transporte.example
  </address>

  <div class="hero" role="img" aria-label="Foto: Frau im karierten Hemd balanciert erschrocken einen wackelnden Stapel Umzugskartons"></div>
  <p class="hero-quote">„Das kann man<br>schon so machen,<br>aber…“</p>
</main>
</body>
</html>
```